Brightpath Letterhead

We would like a letterhead for our company. I have uploaded our logo.

Brightpath Ridge Consulting
1450 W Corliss Ave Ste 310
Arlington, TX 76006
833-517-2906

```html
<!DOCTYPE html>
<html lang="en">
<head>
<meta charset="utf-8">
<title>Brightpath Ridge Consulting — Letterhead</title>
<link rel="stylesheet" href="https://fonts.googleapis.com/css2?family=Jost:wght@400;500;600&display=swap">
<style>
  :root {
    --teal: #155e6b;
    --green: #6cc598;
    --mist: #f6f8f7;
    --footer-cool: #e6edef;
    --footer-mint: #eef7f3;
    --paper: #ffffff;
  }
  * { margin: 0; padding: 0; box-sizing: border-box; }
  html, body { width: 927px; height: 1200px; overflow: hidden; background: var(--paper); }
  .letterhead {
    position: relative;
    width: 927px;
    height: 1200px;
    overflow: hidden;
    background: var(--paper);
    font-family: "Jost", "Helvetica Neue", Arial, sans-serif;
  }
  .top-rule { position: absolute; top: 0; height: 4px; width: 50%; }
  .top-rule--teal { left: 0; background: var(--teal); }
  .top-rule--green { right: 0; background: var(--green); }
  .header-arc {
    position: absolute;
    left: 163px; top: -450px;
    width: 600px; height: 600px;
    border-radius: 50%;
    background: var(--mist);
  }
  .brand {
    position: absolute;
    left: 317px; top: 40px;
    display: flex; align-items: center; gap: 14px;
  }
  .brand__dot {
    width: 40px; height: 40px; border-radius: 50%;
    background: var(--teal);
    flex: none;
  }
  .brand__name {
    color: var(--teal);
    font-weight: 500;
    font-size: 21px;
    line-height: 1.15;
    letter-spacing: 0.12em;
    text-transform: uppercase;
  }
  .footer-panel { position: absolute; top: 1081px; height: 97px; width: 245px; }
  .footer-panel--left { left: 18px; background: var(--footer-cool); }
  .footer-panel--right { left: 664px; background: var(--footer-mint); }
  .footer-ribbons { position: absolute; left: 0; top: 0; }
  .address {
    position: absolute;
    left: 218px; top: 1116px;
    color: var(--paper);
    font-size: 8.6px;
    line-height: 1.45;
    font-weight: 400;
  }
  .phone {
    position: absolute;
    left: 571px; top: 1115px;
    color: var(--paper);
    font-size: 22px;
    font-weight: 600;
    letter-spacing: 0.03em;
    line-height: 30px;
  }
</style>
</head>
<body>
<main class="letterhead">
  <div class="top-rule top-rule--teal"></div>
  <div class="top-rule top-rule--green"></div>
  <div class="header-arc"></div>

  <header class="brand">
    <span class="brand__dot"></span>
    <div class="brand__name">Brightpath Ridge<br>Consulting</div>
  </header>

  <div class="footer-panel footer-panel--left"></div>
  <div class="footer-panel footer-panel--right"></div>

  <svg class="footer-ribbons" width="927" height="1200" viewBox="0 0 927 1200" aria-hidden="true">
    <polygon points="182,1107 393,1107 411,1128 393,1149 182,1149" fill="var(--teal)"/>
    <polygon points="534,1110 745,1110 745,1152 534,1152 516,1131" fill="var(--green)"/>
    <circle cx="463" cy="1129" r="34" fill="none" stroke="var(--teal)" stroke-width="12"/>
    <!-- pin icon -->
    <path d="M206,1119 a5.5,5.5 0 0 1 5.5,5.5 c0,4 -5.5,9.5 -5.5,9.5 s-5.5,-5.5 -5.5,-9.5 a5.5,5.5 0 0 1 5.5,-5.5 z" fill="var(--paper)"/>
    <circle cx="206" cy="1124.5" r="1.9" fill="var(--teal)"/>
    <!-- phone icon -->
    <path d="M547,1123 l3,-1.5 l2.6,4.8 l-1.8,1.4 q1.2,3.4 4.4,5.2 l1.6,-1.6 l4.6,2.8 l-1.6,3 q-6,0.6 -10.4,-4.6 q-3.6,-4.6 -2.4,-9.5 z" fill="var(--paper)"/>
    <path d="M556,1122 a6,6 0 0 1 5,5 M556,1118.5 a9.5,9.5 0 0 1 8.5,8.5" fill="none" stroke="var(--paper)" stroke-width="1.2" stroke-linecap="round"/>
  </svg>

  <address class="address" style="font-style:normal">
    Brightpath Ridge Consulting 1450 W Corliss Ave<br>Ste 310 Arlington, TX 76006
  </address>
  <div class="phone">833-517-2906</div>
</main>
</body>
</html>
```